Chicago Property Management Flyer

We need a brochure/flyer to market our property management services to Chicago property owners. I believe that my preference is single page, double sided, but a bi-fold or tri-fold format may also work. I have provided our logo, and some example images in case that is helpful. Refer to our website at http://www.velmorehq.net/ for more info.

Industry/Entity Type

Property Management

Font styles to use
Sans Serif

```html
<!DOCTYPE html>
<html lang="en">
<head>
<meta charset="utf-8">
<title>Velmore Property Management – Flyer</title>
<link href="https://fonts.googleapis.com/css2?family=Lato:wght@300;400;700&family=Roboto+Condensed:wght@300&family=Roboto:wght@700&display=swap" rel="stylesheet">
<style>
  :root {
    --backdrop: #c9cacc;
    --navy: #33597f;
    --navy-deep: #2b4c6f;
    --heading-blue: #34608f;
    --ink: #2a2a2a;
    --white: #ffffff;
    --strip: #e4e5e7;
  }
  * { box-sizing: border-box; margin: 0; padding: 0; }
  html, body { width: 1200px; height: 800px; overflow: hidden; }
  body { background: var(--backdrop); font-family: "Lato", sans-serif; position: relative; }

  .page { position: absolute; top: 51px; width: 539px; height: 698px; background: var(--white); overflow: hidden; }
  .page--front { left: 45px; }
  .page--back { left: 615px; }

  /* Front */
  .wordmark { position: absolute; text-align: center; color: var(--navy); }
  .wordmark__name { font-weight: 700; font-size: 13.5px; letter-spacing: 0.2px; }
  .wordmark__sub { font-weight: 400; font-size: 9px; letter-spacing: 2.6px; margin-top: 1px; }
  .page--front .wordmark { left: 24px; top: 86px; }
  .wordmark__mark { width: 14px; height: 14px; background: currentColor; margin: 0 auto 8px; }

  .site-url { position: absolute; right: 24px; top: 24px; font-weight: 700; font-size: 16px; color: var(--navy); }

  .front-photo { position: absolute; left: 0; top: 76px; width: 539px; height: 259px;
    background: linear-gradient(180deg, rgba(255,255,255,1) 0%, rgba(225,225,225,0.9) 22%, #a9a9a9 55%, #5e5e5e 100%); }

  .front-panel { position: absolute; left: 0; top: 335px; width: 539px; height: 321px; background: var(--navy); }
  .front-base { position: absolute; left: 0; top: 656px; width: 539px; height: 42px; background: var(--navy-deep); }

  .front-title { position: absolute; left: 150px; top: 354px; font-family: "Roboto Condensed", "Arial Narrow", sans-serif; font-weight: 300;
    font-size: 42px; line-height: 47px; color: var(--white); white-space: nowrap; }
  .front-copy { position: absolute; left: 218px; top: 484px; width: 285px; color: var(--white); }
  .front-copy__lead { font-weight: 700; font-size: 17.5px; line-height: 22px; margin-bottom: 12px; }
  .front-copy p { font-size: 14px; line-height: 18px; margin-bottom: 8px; }

  /* Back */
  .back-header { position: absolute; left: 0; top: 0; width: 539px; height: 117px; background: var(--navy); }
  .back-strip { position: absolute; left: 0; top: 117px; width: 539px; height: 27px; background: var(--strip); }
  .page--back .wordmark { color: var(--white); left: 24px; top: 44px; }
  .back-photo { position: absolute; top: 25px; height: 120px; }
  .back-photo--brick { left: 189px; width: 162px; background: linear-gradient(160deg, #7fa4c9 0%, #8b3f2f 35%, #6e3126 70%, #b7b3a6 100%); }
  .back-photo--stone { left: 364px; width: 152px; background: linear-gradient(160deg, #9bb7d4 0%, #c9b27d 35%, #a88f5e 70%, #c7c4b8 100%); }

  .benefit { position: absolute; color: var(--ink); }
  .benefit h2 { font-weight: 400; font-size: 18px; line-height: 21px; color: var(--heading-blue); margin-bottom: 3px; }
  .benefit p { font-size: 10.3px; line-height: 12.6px; }
  .benefit p.benefit__fine { font-size: 8px; line-height: 10.5px; }
  .col-1 { left: 25px; width: 150px; }
  .col-2 { left: 189px; width: 160px; }
  .col-3 { left: 364px; width: 155px; }
  .row-1 { top: 168px; }
  .row-2 { top: 310px; }

  .skyline { position: absolute; left: 0; top: 440px; width: 539px; height: 216px;
    background: linear-gradient(180deg, rgba(255,255,255,1) 0%, #c9d0d6 30%, #8f9499 60%, #6f6a5e 100%); }
  .contact-bar { position: absolute; left: 0; top: 656px; width: 539px; height: 42px; background: var(--navy);
    color: var(--white); font-family: "Roboto", sans-serif; font-weight: 700; font-size: 12.6px;
    display: flex; align-items: center; justify-content: center; gap: 7px; }
</style>
</head>
<body>
  <section class="page page--front">
    <div class="front-photo" role="img" aria-label="Black and white aerial photo of the Chicago downtown skyline"></div>
    <div class="wordmark">
      <div class="wordmark__mark"></div>
      <div class="wordmark__name">VELMORE PROPERTY</div>
      <div class="wordmark__sub">MANAGEMENT</div>
    </div>
    <div class="site-url">www.velmorehq.net</div>
    <div class="front-panel"></div>
    <div class="front-base"></div>
    <h1 class="front-title">VELMORE PROPERTY<br>MANAGEMENT</h1>
    <div class="front-copy">
      <div class="front-copy__lead">Managing across Chicago’s South, West, and North Sides</div>
      <p>We have been managing properties across Chicago for over a decade.</p>
      <p>Let us leverage our experience and expertise to help ensure success with your properties.</p>
    </div>
  </section>

  <section class="page page--back">
    <div class="back-header"></div>
    <div class="back-strip"></div>
    <div class="wordmark">
      <div class="wordmark__mark"></div>
      <div class="wordmark__name">VELMORE PROPERTY</div>
      <div class="wordmark__sub">MANAGEMENT</div>
    </div>
    <div class="back-photo back-photo--brick" role="img" aria-label="Photo of a red brick Chicago apartment building with iron fence"></div>
    <div class="back-photo back-photo--stone" role="img" aria-label="Photo of a tan brick courtyard apartment building"></div>

    <div class="benefit col-1 row-1">
      <h2>Save Time and Headaches</h2>
      <p>We have a team in place to tackle all aspects of property management for you. Never worry about leasing, tenants, maintenance, regulations, etc.</p>
    </div>
    <div class="benefit col-2 row-1">
      <h2>Increase Income</h2>
      <p>With our experience and market knowledge we can establish optimal rent prices, lease apartments quickly, reduce turnover, and navigate complex housing agency processes to ensure maximum income to you.</p>
    </div>
    <div class="benefit col-3 row-1">
      <h2>Stay Informed</h2>
      <p>With access to all of your property information, documentation, and financials through your online portal of our property management system you and your accountant can stay informed as needed</p>
    </div>
    <div class="benefit col-1 row-2">
      <h2>Maximize Your Investment Assets</h2>
      <p class="benefit__fine">Your properties are expensive assets with lots of potential. Put the right professionals in place to protect, maintain, and maximize their value.</p>
    </div>
    <div class="benefit col-2 row-2">
      <h2>Reduce Expenses, Maximize Profits</h2>
      <p>Maximize your profits by benefitting from our economies of scale, systems and processes, specialized knowledge, industry network, and buying power</p>
    </div>
    <div class="benefit col-3 row-2">
      <h2>Grow Your Investment Portfolio</h2>
      <p>With our management team focused on profitably managing your existing properties, we can then help you expand to future investments</p>
    </div>

    <div class="skyline" role="img" aria-label="Color photo of the Chicago skyline seen from the west side"></div>
    <div class="contact-bar">
      <span>1180 W. Larkin Ave</span><span>|</span><span>Chicago IL 60622</span><span>|</span><span>773-555-0148</span><span>|</span><span>nora@velmorehq.net</span>
    </div>
  </section>
</body>
</html>
```